Flyer für Zeitarbeitsfirma
Zielgruppe
Wir sind eine Zeitarbeitsfirma in der Pflege! Unsere Kunden sind Krankenhäuser und Pflegeheime
Aufgabenstellung
Wir möchten eine Art Flyer als erste Seite einer Bewerbungsmappe.
Überschrift: Bewerbung als Personaldienstleister
Warum K7-CURAVIT?
Wir bieten entscheidende Unterschiede:
1 Tag KOSTENFREI
(Vermindern Sie Ihr Risiko für schlechtes Zeitarbeitspersonal)
5 Tage günstiger Einarbeitungstarif
anschließend erhalten Sie eine Preisgarantie fürs gesamte Jahr
PLUS kostenfreie Übernahme unserer Mitarbeiter
Worauf warten Sie noch?
Wir freuen uns auf eine tolle Zusammenarbeit!
www.kobalt-7.de

```html
<!DOCTYPE html>
<html lang="de">
<head>
<meta charset="utf-8">
<title>K7-CURAVIT – Bewerbung als Personaldienstleister</title>
<link href="https://fonts.googleapis.com/css2?family=Inter+Tight:wght@400;500;700;800&display=swap" rel="stylesheet">
<style>
  :root {
    --ink: #0a0a0a;
    --band: #50b77a;
    --accent: #17963f;
    --muted: #666666;
    --paper: #ffffff;
    --photo-a: #dfe3e6;
    --photo-b: #c9cfd4;
    --photo-c: #2c5d8f;
  }
  * { margin: 0; padding: 0; box-sizing: border-box; }
  html, body { width: 848px; height: 1200px; overflow: hidden; background: var(--paper); }
  body { font-family: "Inter Tight", Arial, sans-serif; color: var(--ink); position: relative; }

  .headline { position: absolute; left: 39px; top: 64px; letter-spacing: -0.04em; }
  .headline__lead { font-size: 38px; font-weight: 500; line-height: 1; }
  .headline__main { font-size: 76px; font-weight: 800; line-height: 1; margin-top: 8px; letter-spacing: -0.055em; }

  .offer-band { position: absolute; left: 0; top: 249px; width: 848px; height: 256px; background: var(--band); color: var(--paper); }
  .offer { position: absolute; letter-spacing: -0.05em; }
  .offer__title { font-size: 50px; font-weight: 700; line-height: 1; }
  .offer__note { font-size: 19px; font-weight: 400; line-height: 1; margin-top: 6px; letter-spacing: -0.04em; }
  .offer--free { left: 47px; top: 48px; }
  .offer--training { left: 42px; top: 141px; }
  .offer--training .offer__note { margin-left: 0; }

  .hero-photo { position: absolute; left: 0; top: 505px; width: 848px; height: 359px;
    background: linear-gradient(100deg, var(--photo-a) 0%, var(--photo-b) 45%, var(--photo-c) 80%, var(--photo-b) 100%); }

  .plus-line { position: absolute; left: 43px; top: 882px; font-size: 31px; font-weight: 700; color: var(--accent); letter-spacing: -0.05em; }

  .closing { position: absolute; left: 42px; top: 1000px; font-size: 39px; font-weight: 400; line-height: 55px; color: var(--muted); letter-spacing: -0.055em; }

  .brand { position: absolute; right: 40px; top: 1075px; display: flex; align-items: center; gap: 10px; }
  .brand__dot { width: 30px; height: 30px; border-radius: 50%; background: var(--accent); }
  .brand__name { font-size: 26px; font-weight: 700; color: var(--accent); letter-spacing: -0.03em; }
</style>
</head>
<body>
  <header class="headline">
    <p class="headline__lead">Bewerbung als</p>
    <h1 class="headline__main">Personaldienstleister</h1>
  </header>

  <section class="offer-band">
    <div class="offer offer--free">
      <p class="offer__title">1 Tag KOSTENFREI</p>
      <p class="offer__note">(Vermindern Sie Ihr Risiko für schlechtes Zeitarbeitspersonal)</p>
    </div>
    <div class="offer offer--training">
      <p class="offer__title">5 Tage günstiger Einarbeitungstarif</p>
      <p class="offer__note">anschließend erhalten Sie eine Preisgarantie fürs gesamte Jahr</p>
    </div>
  </section>

  <div class="hero-photo" role="img" aria-label="Foto: lächelnder Pfleger in blauer Dienstkleidung, im Hintergrund Ärzte und Pflegekräfte im Krankenhausflur"></div>

  <p class="plus-line">+ kostenfreie Übernahme unserer Mitarbeiter</p>

  <p class="closing">Worauf warten Sie noch?<br>Wir freuen uns auf eine tolle<br>Zusammenarbeit!</p>

  <div class="brand">
    <span class="brand__dot"></span>
    <span class="brand__name">K7-CURAVIT</span>
  </div>
</body>
</html>
```